Web Dashboard for manufacturing data

We need a dashboard for website to show statistical information on buttons/cards/tiles. There will be 12 buttons on the screen (laptop, tablet) On these buttons there are several key pieces of information on each button. 1) Largest info is % 0-100%. 2) 4 status colours neutral, green, yellow, red. 3) Title- up to 20 characters 4) target here is an example... target=above 90%.- When these buttons are tapped, they take user to more info for that specific data.
1 page

```html
<!DOCTYPE html>
<html lang="en">
<head>
<meta charset="utf-8">
<title>Manufacturing Dashboard</title>
<link href="https://fonts.googleapis.com/css2?family=Carlito:wght@400;700&display=swap" rel="stylesheet">
<style>
  :root {
    --neutral: #dec6b2;
    --yellow: #e8c064;
    --green: #4a675c;
    --red: #e04a52;
    --white: #ffffff;
    --page: #ffffff;
  }
  * { box-sizing: border-box; margin: 0; padding: 0; }
  html, body {
    width: 1200px; height: 600px; overflow: hidden;
    background: var(--page);
    font-family: "Carlito", "Calibri", Arial, sans-serif;
  }
  .dashboard {
    position: relative;
    width: 1200px; height: 600px;
    padding: 72px 0 0 92px;
    display: grid;
    grid-template-columns: repeat(4, 243px);
    grid-auto-rows: 132px;
    column-gap: 15px;
    row-gap: 30px;
  }
  .tile {
    position: relative;
    border-radius: 11px;
    color: var(--white);
    text-decoration: none;
    display: block;
  }
  .tile--neutral { background: var(--neutral); color: var(--white); --accent: var(--neutral); }
  .tile--yellow  { background: var(--yellow);  --accent: var(--yellow); }
  .tile--green   { background: var(--green);   --accent: var(--green); }
  .tile--red     { background: var(--red);     --accent: var(--red); }

  .tile__badge {
    position: absolute; left: 20px; top: 36px;
    width: 61px; height: 61px; border-radius: 50%;
    background: var(--white);
    display: flex; align-items: center; justify-content: center;
    color: var(--accent);
  }
  .tile__badge svg { width: 36px; height: 36px; fill: currentColor; }
  .tile__text { position: absolute; left: 95px; top: 27px; }
  .tile__title { font-weight: 700; font-size: 17px; line-height: 1; white-space: nowrap; }
  .tile__value { font-size: 26px; line-height: 1; margin-top: 11px; }
  .tile__target { font-size: 13.5px; line-height: 1; margin-top: 7px; }
  .icon-defs { position: absolute; width: 0; height: 0; }
</style>
</head>
<body>
<svg class="icon-defs" aria-hidden="true">
  <defs>
    <symbol id="gear" viewBox="0 0 24 24">
      <g>
        <rect x="10" y="1" width="4" height="22" rx="1"/>
        <rect x="10" y="1" width="4" height="22" rx="1" transform="rotate(45 12 12)"/>
        <rect x="10" y="1" width="4" height="22" rx="1" transform="rotate(90 12 12)"/>
        <rect x="10" y="1" width="4" height="22" rx="1" transform="rotate(135 12 12)"/>
        <circle cx="12" cy="12" r="8"/>
      </g>
      <circle cx="12" cy="12" r="3.5" fill="#fff"/>
    </symbol>
    <symbol id="box" viewBox="0 0 24 24">
      <path d="M12 2 21 7v10l-9 5-9-5V7z"/>
      <path d="M12 12 21 7M12 12 3 7M12 12v10" stroke="#fff" stroke-width="1.3" fill="none"/>
    </symbol>
    <symbol id="factory" viewBox="0 0 24 24">
      <path d="M2 22V10l6 3v-3l6 3V4h3v-2h3v20z"/>
      <rect x="5" y="15" width="3" height="3" fill="#fff"/>
      <rect x="10.5" y="15" width="3" height="3" fill="#fff"/>
      <rect x="16" y="15" width="3" height="3" fill="#fff"/>
    </symbol>
    <symbol id="conveyor" viewBox="0 0 24 24">
      <rect x="3" y="11" width="5" height="5"/>
      <rect x="9.5" y="11" width="5" height="5"/>
      <rect x="16" y="11" width="5" height="5"/>
      <rect x="2" y="18" width="20" height="4" rx="2"/>
      <circle cx="6" cy="20" r="1" fill="#fff"/><circle cx="12" cy="20" r="1" fill="#fff"/><circle cx="18" cy="20" r="1" fill="#fff"/>
    </symbol>
    <symbol id="hand" viewBox="0 0 24 24">
      <path d="M2 15h4v7H2zM7 16h5l3 1h5a2 2 0 0 1 0 3l-6 2H7z"/>
    </symbol>
    <symbol id="cycle" viewBox="0 0 24 24">
      <circle cx="12" cy="12" r="10" fill="none" stroke="currentColor" stroke-width="1.6" stroke-dasharray="4 3"/>
    </symbol>
  </defs>
</svg>

<main class="dashboard">
  <a class="tile tile--neutral" href="#manufacturing-1">
    <span class="tile__badge"><svg viewBox="0 0 24 24"><use href="#gear" x="6" y="1" width="12" height="12"/><use href="#hand" x="0" y="0" width="24" height="24"/></svg></span>
    <div class="tile__text"><div class="tile__title">Manufacturing 1</div><div class="tile__value">80%</div><div class="tile__target">Average= 40%</div></div>
  </a>
  <a class="tile tile--yellow" href="#manufacturing-2">
    <span class="tile__badge"><svg viewBox="0 0 24 24"><use href="#gear" x="7" y="0" width="10" height="10"/><use href="#conveyor"/></svg></span>
    <div class="tile__text"><div class="tile__title">Manufacturing 2</div><div class="tile__value">70%</div><div class="tile__target">Average= 30%</div></div>
  </a>
  <a class="tile tile--green" href="#manufacturing-3">
    <span class="tile__badge"><svg viewBox="0 0 24 24"><use href="#gear"/><use href="#box" x="7" y="7" width="10" height="10"/></svg></span>
    <div class="tile__text"><div class="tile__title">Manufacturing 3</div><div class="tile__value">90%</div><div class="tile__target">Average= 85%</div></div>
  </a>
  <a class="tile tile--red" href="#manufacturing-4">
    <span class="tile__badge"><svg viewBox="0 0 24 24"><use href="#gear" x="1" y="3" width="17" height="17"/><path d="M17 6h3M17 12h5M17 18h3" stroke="currentColor" stroke-width="1.4"/><circle cx="21" cy="6" r="1.4"/><circle cx="22" cy="12" r="1.4"/><circle cx="21" cy="18" r="1.4"/></svg></span>
    <div class="tile__text"><div class="tile__title">Manufacturing 4</div><div class="tile__value">65%</div><div class="tile__target">Average= 55%</div></div>
  </a>

  <a class="tile tile--red" href="#manufacturing-5">
    <span class="tile__badge"><svg viewBox="0 0 24 24"><use href="#gear" x="1" y="1" width="10" height="10"/><use href="#box" x="10" y="10" width="13" height="13"/><path d="M13 4h6v4M4 13v6h4" stroke="currentColor" stroke-width="1.4" fill="none"/></svg></span>
    <div class="tile__text"><div class="tile__title">Manufacturing 5</div><div class="tile__value">50%</div><div class="tile__target">Average= 20%</div></div>
  </a>
  <a class="tile tile--green" href="#manufacturing-6">
    <span class="tile__badge"><svg viewBox="0 0 24 24"><use href="#gear" x="1" y="9" width="13" height="13"/><use href="#gear" x="11" y="1" width="9" height="9"/><use href="#gear" x="13" y="12" width="10" height="10"/></svg></span>
    <div class="tile__text"><div class="tile__title">Manufacturing 6</div><div class="tile__value">60%</div><div class="tile__target">Average= 35%</div></div>
  </a>
  <a class="tile tile--yellow" href="#manufacturing-7">
    <span class="tile__badge"><svg viewBox="0 0 24 24"><use href="#factory"/></svg></span>
    <div class="tile__text"><div class="tile__title">Manufacturing 7</div><div class="tile__value">30%</div><div class="tile__target">Average= 25%</div></div>
  </a>
  <a class="tile tile--neutral" href="#manufacturing-8">
    <span class="tile__badge"><svg viewBox="0 0 24 24"><use href="#gear" x="13" y="3" width="10" height="10"/><use href="#conveyor"/></svg></span>
    <div class="tile__text"><div class="tile__title">Manufacturing 8</div><div class="tile__value">65%</div><div class="tile__target">Average= 55%</div></div>
  </a>

  <a class="tile tile--yellow" href="#manufacturing-9">
    <span class="tile__badge"><svg viewBox="0 0 24 24"><use href="#cycle"/><use href="#gear" x="7" y="7" width="10" height="10"/></svg></span>
    <div class="tile__text"><div class="tile__title">Manufacturing 9</div><div class="tile__value">80%</div><div class="tile__target">Average= 40%</div></div>
  </a>
  <a class="tile tile--red" href="#manufacturing-10">
    <span class="tile__badge"><svg viewBox="0 0 24 24"><use href="#cycle" x="6" y="0" width="12" height="12"/><use href="#gear" x="9" y="3" width="6" height="6"/><path d="M3 12h18v10H3z"/><path d="M3 12l-2 3h9l2-3M21 12l2 3h-9l-2-3" /></svg></span>
    <div class="tile__text"><div class="tile__title">Manufacturing 10</div><div class="tile__value">50%</div><div class="tile__target">Average= 40%</div></div>
  </a>
  <a class="tile tile--neutral" href="#manufacturing-11">
    <span class="tile__badge"><svg viewBox="0 0 24 24"><path d="M3 22v-3h7v3zM5 19l2-8 6-6 2 2-6 6-1 6z"/><circle cx="14" cy="5" r="2"/><rect x="14" y="14" width="8" height="8"/></svg></span>
    <div class="tile__text"><div class="tile__title">Manufacturing 11</div><div class="tile__value">90%</div><div class="tile__target">Average= 85%</div></div>
  </a>
  <a class="tile tile--green" href="#manufacturing-12">
    <span class="tile__badge"><svg viewBox="0 0 24 24"><path d="M3 22V9h15v13h-5v-5H8v5zM19 12h3v10h-3z"/><path d="M5 8V4M9 8V4M13 8V4" stroke="currentColor" stroke-width="1.4"/></svg></span>
    <div class="tile__text"><div class="tile__title">Manufacturing 12</div><div class="tile__value">45%</div><div class="tile__target">Average= 50%</div></div>
  </a>
</main>
</body>
</html>
```